Flyer To Solicit Donations for a Good Cause

Hi. I am running the distance of a marathon race to solicit donations for a charitable cause. I need a well designed flyer to help me solicit support from friends and others. The copy for the flyer is attached. There is a significant amount of written text so it will need to be laid out in a way that is easy to read but also mixes well with some good images and design appeal. I am open to creative ideas. I have also attached my photo and a photo of me shaking hands with Mayor Velidis of Delphi and president of the Concordant Aegean Fellowship. Also there are some photos of the areas. These photos don't have to be used except for the one of me shaking hands with the Mayor and a caption underneath it. Otherwise, I am open to other stock photos or graphics. Feel free to contact me if you have questions. Thank you !

Update: ONE SIDED FLYER

Requirements
Must have
• Photo of the Mayor and Dale with the caption identifying us; All of the copy/text.

```html
<!DOCTYPE html>
<html lang="en">
<head>
<meta charset="utf-8">
<title>Prayer Journey Flyer</title>
<link href="https://fonts.googleapis.com/css2?family=Roboto:wght@400;700&family=Roboto+Condensed:wght@700&display=swap" rel="stylesheet">
<style>
  :root {
    --navy: #0b3d8c;
    --navy-deep: #0a2f6e;
    --blue: #1a8fe3;
    --cyan: #2cb5f5;
    --cyan-light: #6fd0ff;
    --paper: #ffffff;
    --paper-grey: #e9ecef;
    --ink: #1d1d1f;
    --stage: #d9dde2;
  }
  * { box-sizing: border-box; margin: 0; padding: 0; }
  html, body { width: 1200px; height: 900px; overflow: hidden; }
  body { background: var(--stage); font-family: "Roboto", Arial, sans-serif; position: relative; }

  .flyer {
    position: absolute; left: 307px; top: 36px;
    width: 585px; height: 827px; overflow: hidden;
    background: linear-gradient(100deg, var(--paper-grey) 0%, var(--paper) 45%);
    box-shadow: 0 6px 24px rgba(0,0,0,.25);
  }
  .flyer-art { position: absolute; inset: 0; }

  .logo-box {
    position: absolute; left: 20px; top: 27px; width: 162px; height: 68px;
    border: 1.5px solid var(--navy); background: var(--paper);
    color: var(--navy); padding: 10px 0 0 8px;
  }
  .logo-name { font-size: 25px; font-weight: 400; line-height: 1; letter-spacing: .3px; }
  .logo-tagline { font-size: 13.5px; margin-top: 4px; }

  .headline {
    position: absolute; left: 20px; top: 305px; width: 270px;
    font-family: "Roboto Condensed", "Arial Narrow", sans-serif; font-weight: 700;
    font-size: 19.5px; line-height: 1.2; color: var(--navy); text-transform: uppercase;
  }
  .headline .accent { color: var(--blue); font-size: 21px; }

  .story {
    position: absolute; left: 20px; top: 392px; width: 262px;
    font-size: 8.8px; line-height: 1.32; color: var(--ink); text-align: justify;
  }
  .story p + p { margin-top: 8px; }
  .story b { font-weight: 700; }

  .appeal-head {
    position: absolute; left: 283px; top: 406px; width: 292px; height: 42px;
    background: var(--cyan); color: var(--navy-deep);
    font-family: "Roboto Condensed", "Arial Narrow", sans-serif; font-weight: 700;
    font-size: 13.6px; line-height: 1.22; padding: 6px 0 0 14px; text-transform: uppercase;
  }
  .steps {
    position: absolute; left: 298px; top: 462px; width: 272px;
    color: var(--paper); font-size: 9.3px; line-height: 1.4;
  }
  .steps .intro { margin-bottom: 10px; }
  .steps ol { list-style: none; }
  .steps li + li { margin-top: 9px; }
  .step-num {
    display: inline-block; width: 11px; height: 11px; border-radius: 50%;
    background: var(--cyan); color: var(--navy-deep); font-size: 8px; font-weight: 700;
    text-align: center; line-height: 11px; margin-right: 3px; vertical-align: 0;
  }
  .steps .contact { color: var(--cyan-light); font-style: italic; font-weight: 700; }

  .closing-band {
    position: absolute; left: 0; top: 762px; width: 585px; height: 65px;
    background: linear-gradient(180deg, var(--cyan-light) 0%, var(--cyan) 45%, var(--blue) 100%);
    color: var(--navy-deep); text-align: center;
    font-family: "Roboto Condensed", "Arial Narrow", sans-serif; font-weight: 700;
    font-size: 18.5px; line-height: 65px; text-transform: uppercase;
  }
</style>
</head>
<body>
<main class="flyer">
  <svg class="flyer-art" width="585" height="827" viewBox="0 0 585 827">
    <defs>
      <linearGradient id="handshakeTone" x1="0" y1="0" x2="0" y2="1">
        <stop offset="0" stop-color="#6f9fc8"/>
        <stop offset=".5" stop-color="#8b7a6c"/>
        <stop offset="1" stop-color="#9c5a4c"/>
      </linearGradient>
      <linearGradient id="ruinsTone" x1="0" y1="0" x2="0" y2="1">
        <stop offset="0" stop-color="#b7bcc2"/>
        <stop offset=".45" stop-color="#7d7f72"/>
        <stop offset="1" stop-color="#6b6455"/>
      </linearGradient>
    </defs>
    <!-- right panel -->
    <rect class="appeal-panel" x="283" y="290" width="302" height="472" fill="#0b3d8c"/>
    <!-- deep band along the photo -->
    <polygon points="222,0 264,0 210,196 585,350 585,384 190,206" fill="#0b3d8c"/>
    <!-- light stripe under the photo -->
    <polygon points="180,250 585,384 585,397 176,262" fill="#2cb5f5"/>
    <!-- white rule under the photo -->
    <polygon points="210,196 585,350 585,357 205,200" fill="#ffffff"/>
    <!-- handshake photo -->
    <g role="img" aria-label="Photo of Dale shaking hands with Mayor Velidis in an office">
      <polygon points="264,0 585,0 585,348 212,194" fill="url(#handshakeTone)"/>
    </g>
    <!-- squares -->
    <rect x="12" y="150" width="56" height="56" fill="#0b3d8c" transform="rotate(-15 40 178)"/>
    <rect x="96" y="120" width="78" height="78" fill="#2cb5f5" transform="rotate(-15 135 159)"/>
    <rect x="126" y="48" width="40" height="40" fill="#0b3d8c" transform="rotate(-15 146 68)"/>
    <!-- ruins photo -->
    <g role="img" aria-label="Photo of the ancient ruins at Delphi below the mountains">
      <rect x="0" y="594" width="280" height="168" fill="url(#ruinsTone)"/>
    </g>
  </svg>

  <div class="logo-box">
    <div class="logo-name">LOGO HERE</div>
    <div class="logo-tagline">TAGLINE GOES HERE</div>
  </div>

  <h1 class="headline">A special journey for your specific prayers &amp; for an <span class="accent">important ancient cause</span></h1>

  <section class="story">
    <p>This coming <b>April 2016 Dale Hartwell</b> will make a special running journey of <b>26 miles</b> through the <b>ancient lands of Apollo and Athena at Delphi on Mt. Parnassus in Greece</b>.</p>
    <p><b>Dale</b> will adorn his running outfit with special cloth strips that will contain written prayers and petitions of people who will sponsor his journey by making a charitable donation to the Concordant Aegean Fellowship, an organization that preserves the land and the Delphic culture.<b>www.concordant-aegean.org</b></p>
    <p>The concept is simple and very powerful: as Dale runs,your written prayer on a cloth strip will flow and emanate in the wind --- being blessed by the spirits of this ancient and magical land --- asking unto the wind that your prayer be answered. This type of prayer practice dates back to ancient times. The Tibetan culture commonly uses prayer flags with special mantras and symbols.</p>
  </section>

  <h2 class="appeal-head">Will you make a prayer for yourself<br>or a loved and support a good cause?</h2>

  <section class="steps">
    <p class="intro">Here is how to get your prayer started:</p>
    <ol>
      <li><span class="step-num">1</span>Decide what you want your prayer, petition or intention to be.</li>
      <li><span class="step-num">2</span>Define your prayer, petition or intention by writing it down.</li>
      <li><span class="step-num">3</span>Refine it is concise, clear&amp; specific. (18 words or less is ideal for each strip cloth).</li>
      <li><span class="step-num">4</span>Contact <span class="contact">Dale</span> at <span class="contact">dhartwell@hartwellmoss.com</span> and tell him how many prayer cloth strips you wish to obtain. Dale will then send you the cloth for you to write your prayer and send back to him or he will write out the prayer for you. Dale can also answer any questions you may have.</li>
      <li><span class="step-num">5</span>A minimum donation of $50 for each prayer cloth is requested. Checks can be made to the "Hartwell Moss Trust Account/Concordant Aegean Fellowship" and mail to Dale T. Hartwell, Hartwell Moss PLC, 4180 Harbor Lane, Ste. 204 Lakeview, Ohio 44012 or though online payment instructions sent by email from Dale as requested.</li>
    </ol>
  </section>

  <p class="closing-band">Your prayer can make a difference for you &amp; for a good cause !</p>
</main>
</body>
</html>
```